Marketing One-Sheet for Security Deposit Claim Notice

I need a one-sheet flyer formatted for email distribution — optimized as a JPEG/PNG that I can insert into Constant Contact or Outlook. I do not want to attach it to an email, but insert it in the email we send out. I would like it to look professional but engaging. Some images would be good, but want to make sure it reads well if images do not load for the recipients. The text is in the attached Word document, but I am open to changes/ideas that may be better for marketing purposes. I included the URLs for some of the links I would like in the one-sheet that is clickable. The logo for the business is being uploaded on the Word document. Proposed text is also uploaded in a Word document. Thank you.

Target Market(s)

Landlords, Real Estate Agents, Property Managers

Industry/Entity Type

Legal

Requirements
Must have
• Professional but appealing design. The One-sheet is going to be placed in the body of emails, not as an attachment.
Nice to have
• Include our logo for the business and the web links please.
Should not have
• Images can be ok, but it needs to look right if images do not download from the email sent out.

```html
<!DOCTYPE html>
<html lang="en">
<head>
<meta charset="utf-8">
<title>Security Deposit Claim Notice</title>
<link href="https://fonts.googleapis.com/css2?family=Libre+Baskerville:wght@400;700&family=Roboto:wght@300;400;500;700&display=swap" rel="stylesheet">
<style>
:root{
  --red:#e5312f;
  --red-deep:#b81f22;
  --red-text:#d93030;
  --ink:#1b1b1b;
  --band:#222222;
  --body:#3a3a3a;
  --white:#ffffff;
}
*{margin:0;padding:0;box-sizing:border-box}
html,body{width:1200px;height:2918px;overflow:hidden;background:var(--white)}
body{font-family:'Roboto',sans-serif;color:var(--body);position:relative}
section{position:absolute;left:0;width:1200px}

/* hero */
.hero{top:0;height:675px;overflow:hidden}
.hero-photo{position:absolute;inset:0;background:linear-gradient(100deg,#e0302f 0%,#e23a36 45%,#c92a2a 75%,#a61f22 100%)}
.brand{position:absolute;left:75px;top:57px;display:flex;align-items:flex-start;gap:16px;color:var(--white)}
.brand-square{width:26px;height:26px;background:var(--white);margin-top:10px}
.brand-name{font-family:'Libre Baskerville',serif;font-size:38px;line-height:46px;font-weight:400}
.brand-tag{font-size:15px;line-height:18px;margin-top:8px}
.brand-contact{font-size:21px;font-weight:700;line-height:30px;margin-top:8px}
.hero-title{position:absolute;left:75px;top:338px;color:var(--white);font-family:'Libre Baskerville',serif;font-weight:400;font-size:60px;line-height:70px;letter-spacing:1px}
.hero-rule{position:absolute;left:76px;top:494px;width:162px;height:4px;background:var(--white)}
.hero-sub{position:absolute;left:77px;top:526px;color:var(--white);font-size:37px;font-weight:400}

/* benefits */
.benefits{top:675px;height:307px;background:var(--band);display:flex}
.benefit{flex:1;display:flex;flex-direction:column;align-items:center;padding-top:50px;text-align:center;color:var(--white)}
.benefit-icon{width:104px;height:104px;border-radius:50%;background:#2e2e2e;display:flex;align-items:center;justify-content:center}
.benefit-label{font-family:'Libre Baskerville',serif;font-size:26px;line-height:39px;margin-top:22px}

/* split rows */
.row{height:750px;display:flex}
.row-one{top:982px}
.row-two{top:1732px}
.photo{width:600px;height:750px}
.photo-contract{background:linear-gradient(160deg,#d8d4cf 0%,#ebe8e4 45%,#b7b2ad 100%)}
.photo-clients{background:linear-gradient(160deg,#c9c2b6 0%,#e9e6e1 50%,#6f6a66 100%)}
.copy{width:600px;height:750px;position:relative}
.copy-right{padding:70px 48px 0 56px}
.copy-left{padding:68px 58px 0 74px}
.h2{font-family:'Libre Baskerville',serif;color:var(--ink);font-size:30px;line-height:50px;font-weight:400;white-space:nowrap}
.rule-red{width:162px;height:3px;background:var(--red);margin:16px 0 36px}
.fee{font-family:'Libre Baskerville',serif;color:var(--red-text);font-size:34px;font-weight:400;margin-bottom:28px}
.p{font-size:25px;line-height:37px;font-weight:300;color:var(--body)}
.p + .p{margin-top:18px}
.bullets{list-style:none;margin-top:32px}
.bullets li{position:relative;padding-left:45px;font-size:25px;line-height:33px;font-weight:300;margin-bottom:17px;text-align:justify}
.bullets li::before{content:"";position:absolute;left:2px;top:6px;width:20px;height:20px;background:var(--red)}
.commercial{font-family:'Libre Baskerville',serif;color:var(--red-text);font-size:31px;line-height:50px;font-weight:400;margin-bottom:28px;white-space:nowrap}
.copy-left .p{text-align:justify}
.btn-contact{display:inline-block;margin-top:48px;background:var(--ink);color:var(--white);font-weight:500;font-size:25px;padding:12px 43px;border-radius:7px;text-decoration:none}
.hire-link{display:block;margin-top:32px;margin-left:10px;color:var(--red-text);font-size:22px;line-height:30px;text-decoration:underline}

/* footer */
.footer{top:2482px;height:350px;background:linear-gradient(100deg,#d42a2a 0%,#e5312f 50%,#d82c2c 100%)}
.footer-name{position:absolute;left:77px;top:118px;color:var(--white);font-family:'Libre Baskerville',serif;font-size:29px;line-height:46px;white-space:nowrap}
.footer-rule{position:absolute;left:77px;top:226px;width:162px;height:3px;background:var(--white)}
.contact-item{position:absolute;top:74px;display:flex;gap:22px;color:var(--white)}
.contact-web{left:407px}
.contact-phone{left:827px}
.contact-icon{width:96px;height:96px;border-radius:50%;background:var(--band);display:flex;align-items:center;justify-content:center;flex:none}
.contact-label{font-family:'Libre Baskerville',serif;font-size:28px;margin-top:6px}
.contact-value{font-size:27px;margin-top:18px}
.btn-info,.btn-docs{position:absolute;top:218px;height:60px;border-radius:6px;display:flex;align-items:center;justify-content:center;font-size:23px;font-weight:500;text-decoration:underline}
.btn-info{left:399px;width:276px;background:var(--white);color:var(--red-text)}
.btn-docs{left:699px;width:426px;background:var(--ink);color:var(--white)}

.copyright{top:2832px;height:86px;background:var(--band);color:var(--white);font-size:19px;display:flex;align-items:center;justify-content:center}
.code{position:absolute;right:14px;top:44px;font-size:11px}
</style>
</head>
<body>

<section class="hero">
  <div class="hero-photo" role="img" aria-label="Red-toned photo of a hand placing a small model house on a desk"></div>
  <div class="brand">
    <div class="brand-square"></div>
    <div>
      <div class="brand-name">Harborline<br>Landlord Law</div>
      <div class="brand-tag">a Legal Resource for Landlords,<br>Investors &amp; Property Managers</div>
      <div class="brand-contact">HarborlineLaw.com<br>1(877) 555-0142</div>
    </div>
  </div>
  <h1 class="hero-title">SECURITY DEPOSIT<br>CLAIM NOTICE</h1>
  <div class="hero-rule"></div>
  <p class="hero-sub">Keep the tenant’s Security Deposit</p>
</section>

<section class="benefits">
  <div class="benefit">
    <div class="benefit-icon">
      <svg width="84" height="84" viewBox="0 0 84 84" fill="none" stroke="#e5312f" stroke-width="3"><path d="M12 40 L42 14 L72 40"/><rect x="20" y="38" width="44" height="28"/><rect x="36" y="48" width="12" height="18"/><path d="M10 72 L26 66 L38 74 L52 66 L74 72"/></svg>
    </div>
    <div class="benefit-label">Charge against Damages<br>to the Property</div>
  </div>
  <div class="benefit">
    <div class="benefit-icon">
      <svg width="84" height="84" viewBox="0 0 84 84" fill="none" stroke="#e5312f" stroke-width="3"><path d="M10 38 L42 12 L74 38"/><rect x="18" y="36" width="48" height="22"/><rect x="28" y="58" width="52" height="18" rx="3"/><text x="54" y="72" text-anchor="middle" font-family="Roboto,sans-serif" font-size="13" font-weight="700" fill="#e5312f" stroke="none">RENT</text></svg>
    </div>
    <div class="benefit-label">Cover unpaid Rent</div>
  </div>
  <div class="benefit">
    <div class="benefit-icon">
      <svg width="84" height="84" viewBox="0 0 84 84" fill="none" stroke="#e5312f" stroke-width="3"><rect x="18" y="10" width="40" height="56"/><path d="M26 22 H50 M26 30 H50 M26 38 H42"/><path d="M16 60 L30 48 L44 60 V76 H16 Z"/><path d="M70 24 L50 58"/></svg>
    </div>
    <div class="benefit-label">Apply to legal fees and<br>costs</div>
  </div>
</section>

<section class="row row-one">
  <div class="photo photo-contract" role="img" aria-label="Photo of hands signing a contract agreement beside a model house"></div>
  <div class="copy copy-right">
    <h2 class="h2">WE PREPARE SECURITY<br>DEPOSIT CLAIM NOTICES</h2>
    <div class="rule-red"></div>
    <div class="fee">FLAT FEE $350</div>
    <p class="p">Follow Florida law to keep the Deposit</p>
    <p class="p">If the Security Deposit Claim is not made correctly and on time, then:</p>
    <ul class="bullets">
      <li>Tenant is automatically entitled to their full deposit back</li>
      <li>No claim against the deposit can be made</li>
      <li>Tenant can sue and recover the deposit and thousands in legal fees</li>
    </ul>
  </div>
</section>

<section class="row row-two">
  <div class="copy copy-left">
    <h2 class="commercial">For commercial properties,<br>the flat legal fee is $450.</h2>
    <p class="p">There are lawyers that specialize in representing tenants and go after landlords that do not make a proper claim against the security deposit. They sue and win their cases and get thousands of dollars in legal fees against Landlords, even if the tenant owes unpaid rent.</p>
    <a class="btn-contact" href="#contact">Contact Us</a>
    <a class="hire-link" href="#hire">Hire Us to prepare and serve to the tenant the security deposit claim</a>
  </div>
  <div class="photo photo-clients" role="img" aria-label="Photo of a smiling couple on a sofa reviewing documents with an advisor"></div>
</section>

<section class="footer">
  <div class="footer-name">HARBORLINE<br>LANDLORD LAW</div>
  <div class="footer-rule"></div>
  <div class="contact-item contact-web">
    <div class="contact-icon">
      <svg width="60" height="60" viewBox="0 0 60 60" fill="none" stroke="#e5312f" stroke-width="2.5"><circle cx="30" cy="30" r="22"/><ellipse cx="30" cy="30" rx="10" ry="22"/><path d="M8 30 H52 M12 19 H48 M12 41 H48 M30 8 V52"/></svg>
    </div>
    <div>
      <div class="contact-label">Website :</div>
      <div class="contact-value">HarborlineLaw.com</div>
    </div>
  </div>
  <div class="contact-item contact-phone">
    <div class="contact-icon">
      <svg width="56" height="56" viewBox="0 0 56 56" fill="none" stroke="#e5312f" stroke-width="2.5"><path d="M14 8 L22 8 L26 18 L20 22 C23 30 27 34 34 37 L38 31 L48 35 L48 43 C48 46 45 48 42 48 C24 46 10 32 8 14 C8 11 11 8 14 8 Z"/><path d="M32 10 C40 11 45 16 46 24 M32 17 C36 18 38 20 39 24"/></svg>
    </div>
    <div>
      <div class="contact-label">Phone :</div>
      <div class="contact-value">1877-555-0142</div>
    </div>
  </div>
  <a class="btn-info" href="#info">More Information »</a>
  <a class="btn-docs" href="#docs">Request Our Hiring Documents »</a>
</section>

<section class="copyright">
  Copyright © 2025 Harborline Landlord Law. All rights reserved.
  <span class="code">C62</span>
</section>

</body>
</html>
```